Corvella Paintless Dent Removal

Our company works on vehicles removing dents using a highly skilled trade which the metal is massaged out with special tools without disturbing the original paint, hence paintless dent removal. Besides keeping the paint and metal original its also very environmentally friendly since no paint or toxic fillers are used. Also we we are one of the most experienced companies in the business with 25 years

Target Market(s)

Retail Automobile consumers, Auto Dealerships and Auto Body Shops

Industry/Entity Type

Auto Repair

Contact Information for Business Card

Dennis Holbrook
PO Box 538 Ashmere, NY 11952
631-472-8816
corvellapdr@mailnest.example
website corvellapdr.example
youtube corvella paintless dent removal
25 years of experience removing Dents, Dings and Hail Damage

Font styles to use
Serif
Sans Serif

Colors

Designer to choose colors to be used in the design.

Requirements
Must have
• I do like things that are simple but classy and somewhat bold, also I like my logo so that should be somewhat important

```html
<!DOCTYPE html>
<html lang="en">
<head>
<meta charset="utf-8">
<title>Corvella Paintless Dent Removal — Business Cards</title>
<link rel="stylesheet" href="https://fonts.googleapis.com/css2?family=Oswald:wght@500;600&family=Signika:wght@500&family=Questrial&display=swap">
<style>
  :root {
    --navy: #263159;
    --green: #84c225;
    --ink: #1d1d1f;
    --paper: #ffffff;
    --backdrop: #ececec;
    --edge: #cfcfcf;
  }
  * { box-sizing: border-box; margin: 0; padding: 0; }
  html, body { width: 1200px; height: 1200px; overflow: hidden; }
  body { background: var(--backdrop); position: relative; font-family: "Questrial", sans-serif; }

  .card-slot { position: absolute; }
  .card-slot--front-large { left: 272px; top: 142px; }
  .card-slot--back  { left: 72px;  top: 692px; }
  .card-slot--front-small { left: 635px; top: 692px; }
  .card-slot--back, .card-slot--front-small { width: 494px; height: 320px; }
  .card-slot--back .card, .card-slot--front-small .card { transform: scale(0.753); transform-origin: top left; }

  .card {
    position: relative;
    width: 656px; height: 424px;
    background: var(--paper);
    overflow: hidden;
    box-shadow: 0 0 0 1px var(--edge);
  }

  .brand-mark {
    position: absolute;
    display: flex; align-items: center; gap: 12px;
  }
  .brand-mark__dot { width: 22px; height: 22px; border-radius: 50%; background: var(--green); flex: none; }
  .brand-mark__name {
    font-family: "Oswald", sans-serif; font-weight: 600;
    color: var(--navy); font-size: 26px; line-height: 1.05;
    text-transform: uppercase; letter-spacing: 0.5px;
    width: 230px;
  }
  .card--front .brand-mark { left: 345px; top: 44px; }
  .card--back .brand-mark { left: 50%; top: 175px; transform: translateX(-50%); }
  .card--back .brand-mark__name { font-size: 34px; width: 300px; }
  .card--back .brand-mark__dot { width: 28px; height: 28px; }

  .holder-name {
    position: absolute; left: 32px; top: 134px;
    font-family: "Oswald", sans-serif; font-weight: 600;
    font-variant: small-caps; font-size: 62px; line-height: 1;
    color: var(--navy); letter-spacing: 0.5px;
  }
  .card--compact .holder-name { top: 108px; }

  .tagline {
    position: absolute; right: 38px; top: 204px;
    text-align: right; font-family: "Signika", sans-serif; font-weight: 500;
    font-size: 20px; line-height: 26px; color: var(--ink);
  }

  .contact {
    position: absolute; left: 0; right: 0; top: 326px;
    font-size: 16px; color: var(--ink);
  }
  .contact__row { display: flex; justify-content: center; align-items: center; height: 27px; }
  .contact__row--first { padding-left: 14px; }
  .contact__row--second { padding-left: 40px; }
  .contact__item { display: flex; align-items: center; gap: 7px; padding: 0 9px; }
  .contact__item + .contact__item { border-left: 1.5px solid var(--ink); }
  .contact__icon { width: 14px; height: 14px; flex: none; }

  .accent-band { position: absolute; left: 0; bottom: 0; width: 100%; height: 50px; }
  .accent-band--mirrored { transform: scaleX(-1); }
</style>
</head>
<body>

<!-- Front, large -->
<div class="card-slot card-slot--front-large">
  <div class="card card--front">
    <div class="brand-mark"><span class="brand-mark__dot"></span><span class="brand-mark__name">Corvella Paintless Dent Removal</span></div>
    <div class="holder-name">Dennis Holbrook</div>
    <p class="tagline">25 years of experience<br>removing Dents, Dings and Hail Damage</p>
    <div class="contact">
      <div class="contact__row contact__row--first">
        <span class="contact__item"><svg class="contact__icon" viewBox="0 0 14 14"><rect x="0.5" y="2.5" width="13" height="9" fill="none" stroke="#555"/><line x1="3" y1="6" x2="8" y2="6" stroke="#555"/><line x1="3" y1="8.5" x2="6" y2="8.5" stroke="#555"/></svg>PO Box 538 Ashmere, NY 11952</span>
        <span class="contact__item"><svg class="contact__icon" viewBox="0 0 14 14"><path d="M1 5 Q7 0 13 5 L11 6 L9 4.5 H5 L3 6 Z" fill="#222"/><rect x="2.5" y="6.5" width="9" height="6" rx="1" fill="#222"/></svg>631-472-8816</span>
        <span class="contact__item"><svg class="contact__icon" viewBox="0 0 14 14"><circle cx="7" cy="7" r="6" fill="none" stroke="#222" stroke-width="1.2"/><path d="M4 4 L7 5 L6 8 L8 11 L9 8 L11 6 L9 3" fill="#222"/></svg>corvellapdr.example</span>
      </div>
      <div class="contact__row contact__row--second">
        <span class="contact__item"><svg class="contact__icon" viewBox="0 0 14 14"><rect x="0.5" y="2.5" width="13" height="9" fill="none" stroke="#555"/><path d="M0.5 2.5 L7 8 L13.5 2.5" fill="none" stroke="#555"/></svg>corvellapdr@mailnest.example</span>
        <span class="contact__item"><svg class="contact__icon" viewBox="0 0 14 14"><rect x="0" y="2" width="14" height="10" rx="2" fill="#111"/></svg>corvella paintless dent removal</span>
      </div>
    </div>
    <svg class="accent-band" viewBox="0 0 656 50" preserveAspectRatio="none">
      <polygon points="0,7 460,34 0,50" fill="var(--green)"/>
      <polygon points="656,0 488,32 0,50 656,50" fill="var(--navy)"/>
    </svg>
  </div>
</div>

<!-- Back -->
<div class="card-slot card-slot--back">
  <div class="card card--back">
    <div class="brand-mark"><span class="brand-mark__dot"></span><span class="brand-mark__name">Corvella Paintless Dent Removal</span></div>
    <svg class="accent-band" viewBox="0 0 656 50" preserveAspectRatio="none">
      <polygon points="0,7 460,34 0,50" fill="var(--green)"/>
      <polygon points="656,0 488,32 0,50 656,50" fill="var(--navy)"/>
    </svg>
  </div>
</div>

<!-- Front, small -->
<div class="card-slot card-slot--front-small">
  <div class="card card--front card--compact">
    <div class="holder-name">Dennis Holbrook</div>
    <p class="tagline">25 years of experience<br>removing Dents, Dings and Hail Damage</p>
    <div class="contact">
      <div class="contact__row contact__row--first">
        <span class="contact__item"><svg class="contact__icon" viewBox="0 0 14 14"><rect x="0.5" y="2.5" width="13" height="9" fill="none" stroke="#555"/><line x1="3" y1="6" x2="8" y2="6" stroke="#555"/><line x1="3" y1="8.5" x2="6" y2="8.5" stroke="#555"/></svg>PO Box 538 Ashmere, NY 11952</span>
        <span class="contact__item"><svg class="contact__icon" viewBox="0 0 14 14"><path d="M1 5 Q7 0 13 5 L11 6 L9 4.5 H5 L3 6 Z" fill="#222"/><rect x="2.5" y="6.5" width="9" height="6" rx="1" fill="#222"/></svg>631-472-8816</span>
        <span class="contact__item"><svg class="contact__icon" viewBox="0 0 14 14"><circle cx="7" cy="7" r="6" fill="none" stroke="#222" stroke-width="1.2"/><path d="M4 4 L7 5 L6 8 L8 11 L9 8 L11 6 L9 3" fill="#222"/></svg>corvellapdr.example</span>
      </div>
      <div class="contact__row contact__row--second">
        <span class="contact__item"><svg class="contact__icon" viewBox="0 0 14 14"><rect x="0.5" y="2.5" width="13" height="9" fill="none" stroke="#555"/><path d="M0.5 2.5 L7 8 L13.5 2.5" fill="none" stroke="#555"/></svg>corvellapdr@mailnest.example</span>
        <span class="contact__item"><svg class="contact__icon" viewBox="0 0 14 14"><rect x="0" y="2" width="14" height="10" rx="2" fill="#111"/></svg>corvella paintless dent removal</span>
      </div>
    </div>
    <svg class="accent-band accent-band--mirrored" viewBox="0 0 656 50" preserveAspectRatio="none">
      <polygon points="0,7 460,34 0,50" fill="var(--green)"/>
      <polygon points="656,0 488,32 0,50 656,50" fill="var(--navy)"/>
    </svg>
  </div>
</div>

</body>
</html>
```